GUARANTEED WordPress design needed for a sassy, confident charisma coach!

We need a website design for Marla Penrick's brand new, responsive, Wordpress website.
Marla is a trainer / coach who teaches people how to be more charismatic and runs events, publishes video courses and has an ongoing video blog. Her old website is here: www.marlapenrick.co.uk ... but it's now time to have a much better site!
We have a strong idea about the technical components of the website, but we need a designer's eye to create a great style for the site (and provide layered PSD files which our developers will then convert to HTML and CSS).
Marla's brand is sassy, brave, warm and confident. The videos on her existing site give quite a good feel for her personality. We need a clean, stylish and compelling page that isn't too corporate and captures her personality. Every element needs to feel coherent, from fonts and headings to colours and spacing.
The following sites are not exactly what Marla wants (and certainly aren't right in terms of colours) but they give you an idea of the kind of people she is competing against and the area she is operating in:
http://www.tessa-broughley.example/
http://rowanfelsby.example/
Ideally, you will have done something similar and be able to key in on exactly the kind of thing we want: we're not looking to reinvent the wheel. Hopefully you won't mind tweaking a few things if you are close to what we need.
More detail is provided in the word document attached. But in a nutshell we need: a banner, footer, sign-up strap, menu bar, signature and 4 different basic page types. We want bursts of bright colours, contrasted with black and white if possible - sorry we can't be more specific than that...
The word doc also contains some amateur mock-ups as well (the images are also just mockups at this stage) - but although these give a general sense of the structure what we are looking for, we are clearly not designers...so please help! We need a designer's touch!
Kind regards,
Corin
PS The layered PSD versions of the mockup files are available on Cloudvantre: https://files.cloudvantre.example/sh/k72pqa4w1zbtmrd/QXvenlr8Ty3PwMiU6Hs2kYfDb?dl=0
Target Market(s)
Entrepreneurs who need to sell themselves.
Number of Pages Required
4 page

```html
<!DOCTYPE html>
<html lang="en">
<head>
<meta charset="utf-8">
<title>Marla Penrick – Attract, Connect, Influence</title>
<link href="https://fonts.googleapis.com/css2?family=Raleway:wght@400;500;600;700&family=Open+Sans:wght@400;600;700&display=swap" rel="stylesheet">
<style>
:root{
  --accent:#f04a23;
  --accent-dark:#d93a16;
  --cyan:#3fd0ef;
  --cyan-deep:#12b9e2;
  --page:#efefef;
  --card:#ffffff;
  --ink:#1c1c1c;
  --muted:#555555;
  --footer:#474747;
  --white:#ffffff;
  --green:#2fd54a;
  --amber:#e9a11f;
  --coral:#ec5a3e;
}
*{box-sizing:border-box;margin:0;padding:0}
html,body{width:1200px;height:3782px;overflow:hidden}
body{position:relative;background:var(--page);font-family:"Open Sans",Arial,sans-serif;color:var(--ink)}
.abs{position:absolute}

/* nav */
.site-nav{left:0;top:0;width:1200px;height:70px;background:var(--white)}
.brand{left:70px;top:14px;font-family:"Raleway",Arial,sans-serif;font-weight:600;font-size:32px;color:var(--ink);display:flex;align-items:center;gap:10px}
.brand-dot{width:14px;height:14px;border-radius:50%;background:var(--ink)}
.menu{right:52px;top:0;display:flex;gap:62px;height:70px;align-items:center;font-family:"Raleway",Arial,sans-serif;font-size:16px;font-weight:500;letter-spacing:.5px}
.menu a{color:var(--ink);text-decoration:none;position:relative;height:70px;line-height:70px}
.menu a.active::after{content:"";position:absolute;left:-6px;right:-6px;bottom:0;height:5px;background:var(--accent)}

/* hero */
.hero{left:0;top:70px;width:1200px;height:363px;background:var(--white)}
.hero-word{font-family:"Raleway",Arial,sans-serif;line-height:1}
.w-attract{left:200px;top:152px;font-size:58px;font-weight:600;color:var(--accent);letter-spacing:1px}
.w-connect{left:338px;top:228px;font-size:44px;font-weight:400;color:var(--ink);letter-spacing:1px}
.w-influence{left:186px;top:298px;font-size:44px;font-weight:700;color:var(--ink);letter-spacing:1px}
.hero-portrait{left:672px;top:78px;width:200px;height:355px;background:linear-gradient(180deg,#e9e2dc 0%,#e63a3a 35%,#d22a2e 100%);border-radius:90px 90px 0 0}

/* signup band */
.band{left:0;top:433px;width:1200px;height:205px;background:var(--cyan)}
.band-screen{left:70px;top:430px;width:306px;height:196px;background:linear-gradient(180deg,#d6d6d6,#9c9c9c);border-radius:14px;transform:rotate(-8deg)}
.band-copy{left:500px;top:447px;width:560px;font-family:"Raleway",Arial,sans-serif;font-size:28px;line-height:36px;color:#173a4a}
.field{height:38px;background:var(--white);border:none;font-family:"Open Sans",Arial,sans-serif;font-size:16px;color:#555;padding-left:14px;line-height:38px}
.band .field{position:absolute}
.yes{border-radius:50%;background:var(--accent);color:var(--white);font-family:"Raleway",Arial,sans-serif;font-weight:700;display:flex;align-items:center;justify-content:center;text-align:center;box-shadow:0 4px 8px rgba(0,0,0,.25)}
.band-yes{left:929px;top:526px;width:92px;height:92px;font-size:18px;line-height:20px}
.promise{left:568px;top:598px;font-size:13px;font-weight:700;color:#173a4a}

/* posts */
.post{left:48px;width:736px;height:586px;background:var(--card);padding:15px}
.post-banner{position:relative;width:706px;height:338px;overflow:hidden;font-family:"Raleway",Arial,sans-serif}
.post-figure{position:absolute;right:0;top:0;height:100%;width:240px}
.post-body{background:#f3f3f3;height:218px;padding:14px 10px}
.post-title{font-family:"Raleway",Arial,sans-serif;font-size:28px;font-weight:500;color:var(--ink);margin-bottom:12px}
.post-excerpt{font-size:15px;line-height:23px;color:var(--muted)}
.keep{margin-top:22px;display:flex;align-items:center;gap:10px;font-family:"Raleway",Arial,sans-serif;font-size:15px;color:var(--accent);letter-spacing:.5px}

.b-red{background:radial-gradient(circle at 40% 40%,#f47a5c,var(--coral) 60%,#d64a32)}
.b-green{background:var(--green)}
.b-blue{background:var(--cyan-deep)}
.b-amber{background:var(--amber)}

.tag-sm{color:var(--white);font-size:32px;font-weight:400;line-height:38px}
.big-dark{color:#111;font-size:62px;line-height:72px;font-weight:400}

/* sidebar */
.side{left:834px;width:318px;background:var(--card)}
.side-title{font-family:"Raleway",Arial,sans-serif;font-weight:700;font-size:34px;text-align:center;color:var(--ink)}
.popular{text-align:center;color:var(--accent);font-family:"Raleway",Arial,sans-serif;font-weight:700;font-size:18px;margin-top:16px}
.says{list-style:none;margin:14px 20px 0}
.says li{text-align:center;font-size:14px;line-height:20px;color:var(--ink);padding:12px 6px 10px;border-bottom:1px solid #e2e2e2}
.says li:last-child{border-bottom:none}
.says time{display:block;color:var(--accent);font-size:13px;margin-top:6px}
.tags{display:flex;flex-wrap:wrap;justify-content:center;gap:5px;padding:0 14px;margin-top:20px}
.tags span{background:var(--accent);color:var(--white);font-size:12px;line-height:20px;padding:0 7px}
.tags .t-l{font-size:22px;line-height:34px;font-weight:600}
.tags .t-m{font-size:18px;line-height:30px;font-weight:600}
.tags .t-xl{font-size:28px;line-height:40px;font-weight:700}
.promo{position:absolute;left:15px;top:15px;width:288px;height:624px;background:linear-gradient(180deg,#5a5a5a 0%,#3a3836 45%,#2a2825 100%);font-family:"Raleway",Arial,sans-serif;color:var(--white)}
.promo-head{position:absolute;left:10px;top:10px;font-size:32px;line-height:36px;font-weight:500}
.promo-live{position:absolute;left:0;width:100%;top:278px;text-align:center;font-size:84px;font-weight:700}
.promo-note{position:absolute;left:0;width:100%;top:400px;text-align:center;font-size:28px;font-style:normal}
.promo-btn{position:absolute;left:62px;top:530px;width:186px;height:62px;background:var(--cyan);color:#0b2b38;font-family:"Open Sans",Arial,sans-serif;font-weight:600;font-size:20px;display:flex;align-items:center;justify-content:center}

/* pagination */
.pager{left:0;width:832px;top:3200px;display:flex;justify-content:center;gap:16px}
.pager span{width:30px;height:30px;border-radius:50%;border:2px solid #555;font-size:14px;display:flex;align-items:center;justify-content:center;color:#333}
.pager span.current{background:#222;color:var(--white);border-color:#222}

/* footer */
.footer{left:0;top:3301px;width:1200px;height:481px;background:var(--footer)}
.foot-copy{left:0;width:1200px;top:3340px;text-align:center;color:var(--white);font-family:"Raleway",Arial,sans-serif;font-size:30px;line-height:42px}
.foot-yes{left:887px;top:3430px;width:136px;height:136px;font-size:26px;line-height:28px}
.sad{left:0;width:1200px;top:3594px;text-align:center;color:var(--white);font-family:"Raleway",Arial,sans-serif;font-size:28px}
.social{left:0;width:1200px;top:3656px;display:flex;justify-content:center;gap:12px}
.social span{width:38px;height:38px;border-radius:6px;display:block}
.legal{left:0;width:1200px;top:3730px;display:flex;justify-content:center;gap:100px;color:var(--white);font-size:13px;font-weight:600}
</style>
</head>
<body>

<header class="abs site-nav">
  <div class="abs brand">Marla Penrick <span class="brand-dot"></span></div>
  <nav class="abs menu">
    <a class="active">EVENTS</a><a>WORK WITH ME</a><a>CORPORATE</a><a>ABOUT</a><a>CONTACT</a>
  </nav>
</header>

<section class="abs hero">
</section>
<div class="abs hero-word w-attract">ATTRACT</div>
<div class="abs hero-word w-connect">CONNECT</div>
<div class="abs hero-word w-influence">INFLUENCE</div>
<div class="abs hero-portrait" role="img" aria-label="Portrait of Marla in a red dress, hands on hips"></div>

<section class="abs band"></section>
<div class="abs band-screen" role="img" aria-label="Desktop monitor showing a video of Marla"></div>
<p class="abs band-copy">Learn how to unlock the superpower* of your charisma and win all the business you want with this FREE training.</p>
<div class="abs field" style="left:501px;top:547px;width:172px">First name</div>
<div class="abs field" style="left:711px;top:547px;width:171px">Email address</div>
<div class="abs yes band-yes">YES<br>PLEASE!</div>
<p class="abs promise">* Promise to only use your powers for good</p>

<!-- Posts -->
<article class="abs post" style="top:703px">
  <div class="post-banner b-red">
    <div class="abs tag-sm" style="left:28px;top:30px">PUBLIC SPEAKING...</div>
    <div class="abs big-dark" style="left:140px;top:122px">MADE<br>EASY :-)</div>
    <div class="post-figure" role="img" aria-label="Marla speaking with raised hand" style="background:linear-gradient(180deg,#e3604a,#c3301f)"></div>
  </div>
  <div class="post-body">
    <h2 class="post-title">Public speaking...made easy</h2>
    <p class="post-excerpt">Lorem ipsum dolor sit amet, consectetur adipiscing elit. Praesent fringilla tortor et mi convallis, ut scelerisque dui rhoncus. Donec quis lorem malesuada, molestie metus id, vehicula lacus. Pellentesque ultricies venenatis ullamcorper. Sed metus ligula, pharetra id risus eu, fermentum auctor eros.</p>
    <div class="keep">KEEP READING <svg width="36" height="12" viewBox="0 0 36 12"><path d="M0 6H33M27 1l6 5-6 5" stroke="#f04a23" stroke-width="2" fill="none"/></svg></div>
  </div>
</article>

<article class="abs post" style="top:1323px">
  <div class="post-banner b-green">
    <div class="abs tag-sm" style="left:28px;top:30px;font-size:30px;line-height:36px">HOW TO START EVERY DAY<br>IN THE RIGHT FRAME<br>OF MIND!</div>
    <div class="abs" style="left:40px;top:205px;font-size:66px;color:#111;font-style:italic">5 HOT TIPS</div>
    <div class="post-figure" role="img" aria-label="Marla smiling, wearing glasses" style="background:linear-gradient(180deg,#2bc844,#263a8a)"></div>
  </div>
  <div class="post-body">
    <h2 class="post-title">How to start every day in the right frame of mind!</h2>
    <p class="post-excerpt">Lorem ipsum dolor sit amet, consectetur adipiscing elit. Praesent fringilla tortor et mi convallis, ut scelerisque dui rhoncus. Donec quis lorem malesuada, molestie metus id, vehicula lacus. Pellentesque ultricies venenatis ullamcorper. Sed metus ligula, pharetra id risus eu, fermentum auctor eros.</p>
    <div class="keep">KEEP READING <svg width="36" height="12" viewBox="0 0 36 12"><path d="M0 6H33M27 1l6 5-6 5" stroke="#f04a23" stroke-width="2" fill="none"/></svg></div>
  </div>
</article>

<article class="abs post" style="top:1940px">
  <div class="post-banner b-blue">
    <div class="abs" style="left:28px;top:18px;color:#fff;font-size:46px;line-height:62px;font-weight:500">TAKE CHARGE OF YOUR<br><span style="font-size:58px;font-weight:700">STYLE...</span></div>
    <div class="abs" style="left:28px;top:180px;color:#fff;font-size:44px;line-height:62px">...BOOST YOUR<br><span style="font-size:58px">CONFIDENCE</span></div>
    <div class="abs" role="img" aria-label="Style tip card with a red dress and Marla in glasses" style="left:490px;top:118px;width:216px;height:220px;background:linear-gradient(135deg,#ffffff 50%,#e2e2e2)"></div>
  </div>
  <div class="post-body">
    <h2 class="post-title">Take charge of your style...Boost your confidence</h2>
    <p class="post-excerpt">Lorem ipsum dolor sit amet, consectetur adipiscing elit. Praesent fringilla tortor et mi convallis, ut scelerisque dui rhoncus. Donec quis lorem malesuada, molestie metus id, vehicula lacus. Pellentesque ultricies venenatis ullamcorper. Sed metus ligula, pharetra id risus eu, fermentum auctor eros.</p>
    <div class="keep">KEEP READING <svg width="36" height="12" viewBox="0 0 36 12"><path d="M0 6H33M27 1l6 5-6 5" stroke="#f04a23" stroke-width="2" fill="none"/></svg></div>
  </div>
</article>

<article class="abs post" style="top:2568px">
  <div class="post-banner b-amber">
    <div class="abs tag-sm" style="left:28px;top:28px;font-size:32px;line-height:40px">UNFULFILLED? IT'S<br>TIME TO THINK<br>ABOUT YOUR<br>VALUES...</div>
    <div class="abs" style="left:28px;top:280px;color:#111;font-size:36px">DO THIS EXERCISE NOW!</div>
    <div class="post-figure" role="img" aria-label="Marla in a patterned jacket, gesturing" style="background:linear-gradient(180deg,#e0a22a,#6b5a4a)"></div>
  </div>
  <div class="post-body">
    <h2 class="post-title">Unfulfilled? It's time to think about your values...</h2>
    <p class="post-excerpt">Lorem ipsum dolor sit amet, consectetur adipiscing elit. Praesent fringilla tortor et mi convallis, ut scelerisque dui rhoncus. Donec quis lorem malesuada, molestie metus id, vehicula lacus. Pellentesque ultricies venenatis ullamcorper. Sed metus ligula, pharetra id risus eu, fermentum auctor eros.</p>
    <div class="keep">KEEP READING <svg width="36" height="12" viewBox="0 0 36 12"><path d="M0 6H33M27 1l6 5-6 5" stroke="#f04a23" stroke-width="2" fill="none"/></svg></div>
  </div>
</article>

<nav class="abs pager">
  <span class="current">1</span><span>2</span><span>3</span><span>...</span><span>15</span><span>&gt;&gt;</span>
</nav>

<!-- Sidebar -->
<aside class="abs side" style="top:703px;height:481px;padding-top:22px">
  <h3 class="side-title">MARLA SAYS...</h3>
  <p class="popular">POPULAR</p>
  <ul class="says">
    <li>Be more dog: 5 lessons we could learn from our best friends<time>13/07/15</time></li>
    <li>Are you letting your core beliefs hold you back?<time>06/07/15</time></li>
    <li>How I learned to stop worrying and start NETWORKING!<time>30/06/15</time></li>
    <li>Bitchy resting face and other strange - but true - problems<time>23/06/15</time></li>
  </ul>
</aside>

<aside class="abs side" style="top:1210px;height:347px;padding-top:22px">
  <h3 class="side-title">TAGS</h3>
  <div class="tags">
    <span>body language</span>
    <span class="t-l">capsule wardrobe</span>
    <span>confidence</span><span>handshake</span><span>mindset</span><span>rap</span>
    <span>passion</span><span class="t-m">power pose</span>
    <span>presentations</span><span>presence</span>
    <span class="t-xl">rapport</span><span>spring wear</span><span>style</span>
    <span>values</span><span>vision board</span><span>warmth</span>
  </div>
</aside>

<aside class="abs side" style="top:1583px;height:655px">
  <div class="promo" role="img" aria-label="Marla presenting to a live audience">
    <div class="promo-head">UNLOCK<br>THE<br>SUPERPOWER<br>OF CHARISMA</div>
    <div class="promo-live">LIVE</div>
    <div class="promo-note">* Only 6<br>places left.</div>
    <div class="promo-btn">LEARN MORE</div>
  </div>
</aside>

<!-- Footer -->
<footer class="abs footer"></footer>
<p class="abs foot-copy">Hey! Don't go without signing up because you'll miss out on exclusive offers,<br>awesome tips, and weekly motivation in my fab newsletter *.</p>
<div class="abs field" style="left:184px;top:3490px;width:333px;height:53px;line-height:53px">First name</div>
<div class="abs field" style="left:534px;top:3490px;width:333px;height:53px;line-height:53px">Email address</div>
<div class="abs yes foot-yes">YES<br>PLEASE!</div>
<p class="abs sad">* And that'll make me sad :-(</p>
<div class="abs social" aria-label="Social links">
  <span style="background:#3aa6e0"></span>
  <span style="background:#3b5998"></span>
  <span style="background:#1e78b4"></span>
  <span style="background:#c8232c"></span>
  <span style="background:#9a6a4a"></span>
</div>
<div class="abs legal">
  <span>© 2016 Marla Penrick Ltd</span><span>PRIVACY POLICY</span><span>TERMS POLICY</span><span>DISCLAIMERS</span>
</div>

</body>
</html>
```